Brand-new Pediatric Dental Practice needs a website

We are a brand-new dental practice that will specialize in treating children. We want a gorgeous and easily navigable dental practice website that would make a good first impression to potential patients and their parents. It should be modern, SEO-friendly, mobile responsive, and optimized to win new patients.

Target Market(s)

Parents

Industry/Entity Type

Healthcare/Dentistry

Coding

Coded - Design and coding required

Number of Pages Required

4 page

Requirements
Must have
• Use the Wix website building platform. 4 pages: home, meet our dentists, services, contact us
Nice to have
• has a link to our facebook, instagram

```html
<!DOCTYPE html>
<html lang="en">
<head>
<meta charset="utf-8">
<title>Birchwood Pediatric Dentistry</title>
<link href="https://fonts.googleapis.com/css2?family=Nunito+Sans:wght@400;600;700;800;900&display=swap" rel="stylesheet">
<style>
:root{
  --green:#2f9a56;
  --green-dark:#24854a;
  --green-light:#8fd48f;
  --mint:#e4f4e2;
  --ink:#333336;
  --text:#4a4a4c;
  --night:#2d2e30;
  --footer:#444446;
  --white:#ffffff;
}
*{margin:0;padding:0;box-sizing:border-box}
html,body{width:1200px;height:5017px;overflow:hidden}
body{position:relative;font-family:"Nunito Sans",Arial,sans-serif;color:var(--text);background:var(--white)}
.abs{position:absolute}
.ph{position:absolute}
/* header / hero */
.hero{position:absolute;left:0;top:0;width:1200px;height:725px;background:radial-gradient(ellipse at 62% 45%,#e9c2a4 0%,#c79a78 18%,#6a6a3a 42%,#39521f 70%,#23381a 100%)}
.topbar{position:absolute;left:0;top:0;width:1200px;height:117px;background:linear-gradient(#1d2a16e6,#1d2a1600)}
.brand{position:absolute;left:55px;top:38px;display:flex;align-items:center;gap:10px;color:var(--white);font-weight:800;font-size:24px}
.brand i{width:30px;height:30px;border-radius:50%;background:var(--green-light);display:block}
.nav a{position:absolute;top:49px;color:var(--white);font-size:14px;text-decoration:none;font-weight:600}
.nav a.active{color:var(--green-light)}
.login{position:absolute;left:1060px;top:46px;display:flex;align-items:center;gap:12px;color:var(--white);font-size:14px;font-weight:600}
.hero-name{position:absolute;left:195px;top:300px;color:var(--green-light);font-weight:900;font-size:34px}
.hero h1{position:absolute;left:55px;top:422px;color:var(--white);font-weight:800;font-size:47px;letter-spacing:.2px}
.hero p{position:absolute;left:62px;top:490px;color:var(--white);font-size:24px}
.btn{position:absolute;display:flex;align-items:center;justify-content:center;border-radius:30px;font-size:15px;font-weight:700;text-decoration:none;text-transform:uppercase}
.btn-fill{background:var(--green);color:var(--white);border:3px solid var(--green-light)}
.btn-line{background:var(--white);color:var(--green);border:3px solid var(--green)}
.stripe{position:absolute;left:0;width:1200px;height:8px;background:linear-gradient(90deg,var(--green) 0%,var(--green) 40%,var(--green-light) 100%)}
/* features */
.feature{position:absolute;top:818px;width:250px}
.feature h3{margin-top:30px;font-size:22px;font-weight:700;color:var(--ink)}
.feature p{margin-top:10px;font-size:14px;line-height:23px}
.vline{position:absolute;top:814px;width:1px;height:200px;background:#cfcfcf}
/* why */
.why{position:absolute;left:0;top:1105px;width:1200px;height:545px;background:var(--mint)}
.why-photo{left:162px;top:91px;width:360px;height:360px;border-radius:14px;background:linear-gradient(135deg,#2d6fb8 0%,#c9a080 45%,#e8e8ee 80%,#5aa0d8 100%)}
.why h2{position:absolute;left:635px;top:130px;font-size:33px;font-weight:800;color:var(--ink)}
.why .rule{position:absolute;left:635px;top:191px;width:102px;height:2px;background:var(--green-light)}
.why p{position:absolute;left:635px;top:215px;width:405px;font-size:14px;line-height:22.5px}
/* section titles */
.sec-title{position:absolute;left:0;width:1200px;text-align:center;font-size:33px;font-weight:800;color:var(--ink)}
.sec-title.light{color:var(--white)}
.bars{position:absolute;left:506px;width:192px;height:4px}
.bars span{position:absolute;top:0;width:56px;height:4px;background:var(--green-light)}
.bars span:nth-child(1){left:0}.bars span:nth-child(2){left:69px}.bars span:nth-child(3){left:137px}
.bars.mid-dark span:nth-child(2){background:var(--ink)}
.bars.first-dark span:nth-child(1){background:var(--ink)}
.bars.first-white span:nth-child(1){background:#e8e8e8}
/* dentists */
.dentist{position:absolute;top:1858px;width:274px;height:565px;border-radius:10px;background:var(--green);overflow:hidden;color:var(--white)}
.dentist .photo{position:absolute;left:0;top:0;width:274px;height:294px}
.dentist .role{position:absolute;left:24px;top:337px;font-size:13px;color:#d8efdd}
.dentist h3{position:absolute;left:24px;top:370px;font-size:22px;font-weight:800}
.dentist p{position:absolute;left:24px;top:408px;width:230px;font-size:14px;line-height:22px}
.socials{position:absolute;left:26px;top:512px;display:flex;gap:10px}
.socials i{width:27px;height:27px;border-radius:50%;background:#e9f5ec;display:block}
/* reviews */
.reviews{position:absolute;left:0;top:2600px;width:1200px;height:650px;background:radial-gradient(ellipse at 65% 20%,#6b5048 0%,#3e3a3a 30%,#2d2e30 60%,#232426 100%)}
.review{position:absolute;top:226px;width:274px;height:322px;background:var(--white);border-radius:8px;padding:40px 25px 0}
.quote{position:absolute;top:176px;font-family:Georgia,serif;font-size:110px;line-height:110px;font-weight:700;color:var(--green-light)}
.review h4{font-size:15px;font-weight:800;color:var(--ink)}
.stars{display:flex;gap:6px;margin-top:6px}
.review p{margin-top:16px;font-size:14px;line-height:22.3px}
/* services */
.service{position:absolute;top:3456px;width:252px}
.service .photo{width:252px;height:170px;border-radius:10px}
.service .tag{margin-top:30px;padding-left:17px;font-size:13px;text-transform:uppercase;color:var(--ink)}
.service h3{margin-top:8px;padding-left:17px;font-size:22px;font-weight:800;color:var(--green)}
.service p{margin-top:8px;padding-left:17px;font-size:14px;line-height:22.5px}
.service .under{position:absolute;left:0;top:384px;width:252px;height:4px;background:var(--green)}
.service.soft .under{background:var(--green-light)}
/* contact */
.contact{position:absolute;left:0;top:4032px;width:1200px;height:341px;background:var(--mint)}
.contact .kicker{position:absolute;left:162px;top:78px;font-size:19px;color:var(--green)}
.contact h2{position:absolute;left:162px;top:117px;font-size:26px;line-height:33px;font-weight:800;color:var(--ink)}
.contact .cname{position:absolute;left:540px;top:98px;font-size:28px;font-weight:900;color:var(--green)}
.call{position:absolute;left:461px;top:212px;display:flex;align-items:center;gap:16px}
.call div{font-size:17px;font-weight:800;line-height:28px;color:var(--ink)}
.hours{position:absolute;left:736px;top:0;width:302px;height:341px;background:var(--green);color:var(--white);padding:62px 34px 0}
.hours h3{font-size:25px;font-weight:800}
.hours .row{margin-top:10px;font-size:13px;padding-bottom:8px;border-bottom:1px solid #7cc598}
.hours .row:first-of-type{margin-top:16px}
.hours .info{display:flex;align-items:center;gap:12px;font-size:13px;margin-top:12px}
.hours .info.first{margin-top:26px}
/* footer */
.footer{position:absolute;left:0;top:4381px;width:1200px;height:636px;background:var(--footer);color:var(--white)}
.footer h4{position:absolute;top:83px;font-size:17px;font-weight:800;color:var(--green-light)}
.footer .about{position:absolute;left:162px;top:128px;width:380px;font-size:14px;line-height:23px}
.footer ul{position:absolute;top:128px;list-style:none;font-size:13px;line-height:22.4px}
.footer .divider{position:absolute;left:162px;top:306px;width:876px;height:1px;background:#6a6a6c}
.f-brand{position:absolute;left:0;top:378px;width:1200px;text-align:center}
.f-brand .dot{width:70px;height:70px;border-radius:50%;background:var(--green-light);margin:0 auto 14px}
.f-brand .name{font-size:34px;font-weight:700}
.f-brand .sub{font-size:12px;letter-spacing:5px;margin-top:4px}
.f-social{position:absolute;left:0;top:515px;width:1200px;display:flex;justify-content:center;gap:16px}
.f-social i{width:43px;height:43px;border-radius:50%;background:var(--green-light);display:block}
.copy{position:absolute;left:0;top:577px;width:1200px;text-align:center;font-size:13px;color:var(--green-light)}
</style>
</head>
<body>

<!-- HERO -->
<section class="hero">
  <div class="ph" role="img" aria-label="Photo of a smiling young girl lying on the grass" style="left:0;top:0;width:1200px;height:725px"></div>
  <div class="topbar"></div>
  <div class="brand"><i></i>Birchwood</div>
  <nav class="nav">
    <a class="active" style="left:390px">Home</a>
    <a style="left:471px">Meet Our Dentists</a>
    <a style="left:637px">Services</a>
    <a style="left:734px">Contact Us</a>
  </nav>
  <div class="login">
    <svg width="24" height="24" viewBox="0 0 24 24"><circle cx="12" cy="12" r="10.5" fill="none" stroke="#8fd48f" stroke-width="2"/><circle cx="12" cy="9.5" r="3.5" fill="#8fd48f"/><path d="M5.5 18.5c2-3 4-4 6.5-4s4.5 1 6.5 4" fill="#8fd48f"/></svg>
    Log In
  </div>
  <div class="hero-name">Birchwood</div>
  <h1>Smiles All Around</h1>
  <p>You'll leave our clinic with a Smile</p>
  <a class="btn btn-fill" style="left:129px;top:561px;width:253px;height:49px">Book Appointment</a>
</section>
<div class="stripe" style="top:725px"></div>

<!-- FEATURES -->
<div class="feature" style="left:170px">
  <svg width="80" height="70" viewBox="0 0 80 70" fill="none" stroke="#2f9a56" stroke-width="2.2"><path d="M8 14c0-8 10-10 18-6 8-4 18-2 18 6 0 8-4 12-5 22-1 8-3 14-6 14-3 0-3-12-7-12s-4 12-7 12c-3 0-5-6-6-14C12 26 8 22 8 14z"/><circle cx="46" cy="44" r="14"/><path d="M46 37v14M39 44h14"/></svg>
  <h3>Best Dentists</h3>
  <p>Lorem ipsum dolor sit amet, consectetur adipiscing elit. Aliquam quis semper felis.</p>
</div>
<div class="vline" style="left:436px"></div>
<div class="feature" style="left:470px">
  <svg width="80" height="70" viewBox="0 0 80 70" fill="none" stroke="#2f9a56" stroke-width="2.2"><path d="M14 14c0-8 10-10 18-6 8-4 18-2 18 6 0 8-4 12-5 22-1 8-3 14-6 14-3 0-3-12-7-12s-4 12-7 12c-3 0-5-6-6-14C18 26 14 22 14 14z"/><path d="M6 2l10 26M62 62l14-22"/><circle cx="78" cy="37" r="3"/></svg>
  <h3>Quick Examination</h3>
  <p>Lorem ipsum dolor sit amet, consectetur adipiscing elit. Aliquam quis semper felis.</p>
</div>
<div class="vline" style="left:736px"></div>
<div class="feature" style="left:770px">
  <svg width="80" height="70" viewBox="0 0 80 70" fill="none" stroke="#2f9a56" stroke-width="2.2"><path d="M10 16c0-8 10-10 18-6 8-4 18-2 18 6 0 8-4 12-5 22-1 8-3 14-6 14-3 0-3-12-7-12s-4 12-7 12c-3 0-5-6-6-14C14 28 10 24 10 16z"/><path d="M6 4v8M2 8h8M40 2v6M37 5h6"/><circle cx="48" cy="44" r="13"/><path d="M42 44l4 4 8-8"/></svg>
  <h3>Painless Procedures</h3>
  <p>Lorem ipsum dolor sit amet, consectetur adipiscing elit. Aliquam quis semper felis.</p>
</div>

<!-- WHY -->
<section class="why">
  <div class="ph why-photo" role="img" aria-label="Photo of a boy in sunglasses having his teeth checked"></div>
  <h2>Why Birchwood?</h2>
  <div class="rule"></div>
  <p>Lorem ipsum dolor sit amet, consectetur adipiscing elit, sed do eiusmod tempor incididunt ut labore et dolore magna aliqua. Ut enim ad minim veniam, quis nostrud exercitation ullamco laboris nisi ut aliquip ex ea commodo consequat. Duis aute irure dolor in reprehenderit in voluptate velit esse cillum dolore eu fugiat nulla pariatur. Excepteur sint occaecat cupidatat non proident, sunt in culpa qui officia deserunt mollit anim id est laborum.</p>
</section>

<!-- DENTISTS -->
<h2 class="sec-title" style="top:1733px">Meet Our Dentists</h2>
<div class="bars mid-dark" style="top:1808px"><span></span><span></span><span></span></div>

<article class="dentist" style="left:162px">
  <div class="photo" role="img" aria-label="Portrait photo of a dentist in a white coat" style="background:linear-gradient(160deg,#f2f2f2,#d8d8da 60%,#bfc0c4)"></div>
  <div class="role">DENTIST</div><h3>Dentist Name</h3>
  <p>Lorem ipsum dolor sit amet, consectetur adipiscing elit. Aliquam quis semper felis.</p>
  <div class="socials"><i></i><i></i><i></i></div>
</article>
<article class="dentist" style="left:462px">
  <div class="photo" role="img" aria-label="Portrait photo of a dentist holding a blue folder" style="background:linear-gradient(160deg,#f0f0f0,#d6d9de 55%,#6f9fd0)"></div>
  <div class="role">DENTIST</div><h3>Dentist Name</h3>
  <p>Lorem ipsum dolor sit amet, consectetur adipiscing elit. Aliquam quis semper felis.</p>
  <div class="socials"><i></i><i></i><i></i></div>
</article>
<article class="dentist" style="left:764px">
  <div class="photo" role="img" aria-label="Portrait photo of a dentist in blue scrubs" style="background:linear-gradient(160deg,#f3f3f3,#d9dde0 50%,#45a9d6)"></div>
  <div class="role">DENTIST</div><h3>Dentist Name</h3>
  <p>Lorem ipsum dolor sit amet, consectetur adipiscing elit. Aliquam quis semper felis.</p>
  <div class="socials"><i></i><i></i><i></i></div>
</article>

<a class="btn btn-line" style="left:452px;top:2482px;width:296px;height:49px">Meet All Our Dentists</a>

<!-- REVIEWS -->
<section class="reviews" role="img" aria-label="Dark background photo of a close-up dental checkup">
  <h2 class="sec-title light" style="top:80px">Patient’s Reviews</h2>
  <div class="bars first-white" style="top:146px"><span></span><span></span><span></span></div>

  <div class="quote" style="left:184px">“</div>
  <div class="review" style="left:162px">
    <h4>Patients Name</h4>
    <div class="stars"><svg width="100" height="14" viewBox="0 0 100 14"><g fill="#2f9a56"><path id="s" d="M7 0l2 5h5l-4 3 1.5 5L7 10l-4.5 3L4 8 0 5h5z"/><use href="#s" x="20"/><use href="#s" x="40"/><use href="#s" x="60"/><use href="#s" x="80"/></g></svg></div>
    <p>Lorem ipsum dolor sit amet, consectetur adipiscing elit, sed do eiusmod tempor incididunt ut labore et dolore magna aliqua. Ut enim ad minim veniam, quis nostrud exercitation ullamco laboris nisi ut aliquip ex ea commodo consequat.</p>
  </div>
  <div class="quote" style="left:484px">“</div>
  <div class="review" style="left:462px">
    <h4>Patients Name</h4>
    <div class="stars"><svg width="100" height="14" viewBox="0 0 100 14"><g fill="#2f9a56"><use href="#s"/><use href="#s" x="20"/><use href="#s" x="40"/><use href="#s" x="60"/><use href="#s" x="80"/></g></svg></div>
    <p>Lorem ipsum dolor sit amet, consectetur adipiscing elit, sed do eiusmod tempor incididunt ut labore et dolore magna aliqua. Ut enim ad minim veniam, quis nostrud exercitation ullamco laboris nisi ut aliquip ex ea commodo consequat.</p>
  </div>
  <div class="quote" style="left:786px">“</div>
  <div class="review" style="left:764px">
    <h4>Patients Name</h4>
    <div class="stars"><svg width="100" height="14" viewBox="0 0 100 14"><g fill="#2f9a56"><use href="#s"/><use href="#s" x="20"/><use href="#s" x="40"/><use href="#s" x="60"/><use href="#s" x="80"/></g></svg></div>
    <p>Lorem ipsum dolor sit amet, consectetur adipiscing elit, sed do eiusmod tempor incididunt ut labore et dolore magna aliqua. Ut enim ad minim veniam, quis nostrud exercitation ullamco laboris nisi ut aliquip ex ea commodo consequat.</p>
  </div>
</section>

<!-- SERVICES -->
<h2 class="sec-title" style="top:3332px">Our Services</h2>
<div class="bars first-dark" style="top:3405px"><span></span><span></span><span></span></div>

<article class="service" style="left:56px">
  <div class="photo" role="img" aria-label="Photo of a dental check with a mirror in an open mouth" style="background:radial-gradient(ellipse at 60% 55%,#c77f72,#5a3a34 45%,#151515 85%)"></div>
  <div class="tag">Teeth</div><h3>Dental Services</h3>
  <p>Lorem ipsum dolor sit amet, consectetur adipiscing elit. Maecenas sagittis mi faucibus risus auctor scelerisque.</p>
  <div class="under"></div>
</article>
<article class="service" style="left:335px">
  <div class="photo" role="img" aria-label="Photo of a child in a dental chair under a lamp" style="background:radial-gradient(ellipse at 50% 60%,#8f99a6,#3f4650 50%,#16181b 90%)"></div>
  <div class="tag">Cosmetic</div><h3>Dentistry</h3>
  <p>Lorem ipsum dolor sit amet, consectetur adipiscing elit. Maecenas sagittis mi faucibus risus auctor scelerisque.</p>
  <div class="under"></div>
</article>
<article class="service soft" style="left:613px">
  <div class="photo" role="img" aria-label="Photo of a child having teeth examined by gloved hands" style="background:linear-gradient(135deg,#d8c0b0,#e0b49a 45%,#9fb6d4 80%)"></div>
  <div class="tag">The Best Solution</div><h3>Dental Bridges</h3>
  <p>Lorem ipsum dolor sit amet, consectetur adipiscing elit. Maecenas sagittis mi faucibus risus auctor scelerisque.</p>
  <div class="under"></div>
</article>
<article class="service soft" style="left:890px">
  <div class="photo" role="img" aria-label="Photo of a laughing girl on a dark background" style="background:radial-gradient(ellipse at 55% 50%,#c49276,#5e3f30 45%,#161311 85%)"></div>
  <div class="tag">Beautify Your Smile</div><h3>Teeth Whitening</h3>
  <p>Lorem ipsum dolor sit amet, consectetur adipiscing elit. Maecenas sagittis mi faucibus risus auctor scelerisque.</p>
  <div class="under"></div>
</article>

<a class="btn btn-fill" style="left:454px;top:3906px;width:292px;height:49px">View All Our Services</a>

<!-- CONTACT -->
<section class="contact">
  <div class="kicker">Interested?</div>
  <h2>CONTACT US AND<br>SCHEDULE YOUR VISIT</h2>
  <div class="cname">Birchwood</div>
  <a class="btn btn-fill" style="left:164px;top:213px;width:249px;height:47px">Book Appointment</a>
  <div class="call">
    <svg width="48" height="48" viewBox="0 0 48 48" fill="none" stroke="#2f9a56" stroke-width="2.2"><path d="M14 10l6 8-4 4c2 5 6 9 11 11l4-4 8 6-4 6C22 40 8 26 8 14z"/><path d="M28 8a12 12 0 0 1 12 12M28 14a6 6 0 0 1 6 6"/></svg>
    <div>FREE CALL 24/7<br>+1 555 0142 020</div>
  </div>
  <div class="hours">
    <h3>Office Hours</h3>
    <div class="row">Monday - Friday : 8am - 8pm</div>
    <div class="row">Saturday : 8am - 6pm</div>
    <div class="row">Sunday : 8am - 6pm</div>
    <div class="info first"><svg width="14" height="18" viewBox="0 0 14 18"><path d="M7 0a7 7 0 0 1 7 7c0 5-7 11-7 11S0 12 0 7a7 7 0 0 1 7-7z" fill="#fff"/><circle cx="7" cy="7" r="2.6" fill="#2f9a56"/></svg>123 your address details</div>
    <div class="info"><svg width="16" height="12" viewBox="0 0 16 12" fill="none" stroke="#fff" stroke-width="1.4"><rect x="1" y="1" width="14" height="10"/><path d="M1 1l7 6 7-6"/></svg>hello@birchwood.example</div>
  </div>
</section>
<div class="stripe" style="top:4373px"></div>

<!-- FOOTER -->
<footer class="footer">
  <h4 style="left:162px">Who We Are</h4>
  <p class="about">Lorem ipsum dolor sit amet, consectetur adipiscing elit, sed do eiusmod tempor incididunt ut labore et dolore magna aliqua. Ut enim ad minim veniam, quis nostrud exercitation ullamco laboris nisi ut aliquip ex ea commodo consequat.</p>
  <h4 style="left:649px">Useful Links</h4>
  <ul style="left:649px"><li>Home</li><li>About Us</li><li>Meet Our Dentist</li><li>Contact Us</li><li>Terms &amp; Condition</li><li>Privacy Policy</li></ul>
  <h4 style="left:896px">Our Services</h4>
  <ul style="left:896px"><li>Home</li><li>About Us</li><li>Meet Our Dentist</li><li>Contact Us</li><li>Terms &amp; Condition</li><li>Privacy Policy</li></ul>
  <div class="divider"></div>
  <div class="f-brand"><div class="dot"></div><div class="name">Birchwood</div></div>
  <div class="f-social"><i></i><i></i><i></i><i></i><i></i></div>
  <div class="copy">Copyright © 2022 Birchwood. All rights reserved.</div>
</footer>

</body>
</html>
```